Software as a Service to manage Home Care Management

We need a web site designed for Home Care Management Software as a Service product, that facilitates Home Care organizations to manage and schedule carers to visit client homes. We want a modern look and feel using our existing logo.

Target Market(s)

Home Care Management organizations. Product is similar to: https://kelvantro.co/

Coding

Coded - Design and coding required

Number of Pages Required

3 page

```html
<!DOCTYPE html>
<html lang="en">
<head>
<meta charset="utf-8">
<title>Visitwell – Home Care Management</title>
<link href="https://fonts.googleapis.com/css2?family=Cinzel:wght@500;600;700&family=Poppins:wght@400;500;600;700&display=swap" rel="stylesheet">
<style>
:root{
  --pink:#f9417e;
  --pink-soft:#fb8db0;
  --dark:#3a3536;
  --darker:#2f2b2c;
  --ink:#262224;
  --grey:#555;
  --white:#fff;
}
*{box-sizing:border-box;margin:0;padding:0}
html,body{width:1200px;height:3671px;overflow:hidden}
body{position:relative;font-family:"Poppins",sans-serif;color:var(--ink);background:var(--white)}
.abs{position:absolute}
.serif{font-family:"Cinzel",serif}

/* header */
.site-header{left:0;top:0;width:1200px;height:83px;background:var(--white);z-index:5}
.brand{left:32px;top:18px;display:flex;align-items:center;gap:12px}
.brand-mark{width:40px;height:40px;border-radius:50%;background:var(--pink)}
.brand-name{font-family:"Cinzel",serif;font-weight:600;font-size:30px;line-height:1;color:var(--ink)}
.brand-tag{font-family:"Cinzel",serif;font-size:11px;letter-spacing:2.5px;color:var(--ink)}
.main-nav{left:463px;top:31px;display:flex;gap:29px;font-size:16px;font-weight:500}
.login{left:880px;top:25px;width:98px;height:34px;border:2px solid var(--ink);border-radius:17px;font-size:15px;font-weight:500;text-align:center;line-height:30px}
.demo-btn{left:1008px;top:0;width:192px;height:83px;background:var(--pink);color:var(--white);padding:18px 0 0 36px;font-size:14px;line-height:1.2}
.demo-btn strong{display:block;font-size:22px;font-weight:600}

/* hero */
.hero-photo{left:0;top:83px;width:1200px;height:829px;background:linear-gradient(100deg,#f1ede8 0%,#ebe3da 38%,#c9b9a5 60%,#5d79a8 78%,#d8b15c 100%)}
.hero-title{left:131px;top:198px;font-family:"Cinzel",serif;font-weight:600;font-size:60px;line-height:59px;color:var(--ink)}
.hero-list{left:131px;top:396px;list-style:none;font-size:20px}
.hero-list li{display:flex;align-items:center;gap:12px;height:37px}
.hero-btn{left:132px;top:529px;width:214px;height:54px;border-radius:27px;background:var(--pink);color:var(--white);font-size:17px;font-weight:600;display:flex;align-items:center;justify-content:center;gap:8px}

/* welcome */
.welcome{left:0;top:845px;width:1200px;text-align:center}
.welcome h1{font-family:"Cinzel",serif;font-weight:500;font-size:44px;line-height:1}
.welcome h2{font-family:"Cinzel",serif;font-weight:500;font-size:28px;margin-top:4px}
.welcome p{font-size:17px;line-height:27px;margin:12px auto 0;width:740px}

.audiences{left:131px;top:1052px;width:940px;display:flex}
.audience{width:313px;text-align:center;height:216px}
.audience+.audience{border-left:1px solid #bbb}
.audience .icon{width:86px;height:86px;margin:3px auto 0;border-radius:50%;border:3px solid var(--pink);display:flex;align-items:center;justify-content:center}
.audience .icon span{width:70px;height:70px;border-radius:50%;background:var(--pink)}
.audience h3{font-family:"Cinzel",serif;font-weight:600;font-size:20px;margin-top:14px}
.audience p{font-size:13px;line-height:19px;color:var(--grey);width:215px;margin:10px auto 0}

/* services */
.services-band{left:0;top:1340px;width:1200px;height:870px}
.service{border-radius:50%;background:var(--dark);display:flex;align-items:center;justify-content:center}
.service.featured{background:var(--pink)}
.service-photo{border-radius:50%;display:flex;flex-direction:column;align-items:center;justify-content:flex-end;color:var(--white);font-weight:600;font-size:24px;line-height:29px;text-align:center;text-transform:uppercase;padding-bottom:22px;border:4px solid var(--white)}
.service-photo .go{margin-top:10px;width:28px;height:28px;border:2px solid var(--pink);border-radius:50%;display:flex;align-items:center;justify-content:center}

.what-title{left:650px;top:1808px;font-size:42px;font-weight:700;color:var(--white)}
.what-text{left:650px;top:1886px;width:425px;font-size:17px;line-height:24px;color:#eee}
.pill{background:var(--pink);color:var(--white);border-radius:22px;display:flex;align-items:center;justify-content:center;font-weight:500}

/* news */
.news-title{left:0;top:2277px;width:1200px;text-align:center;font-size:34px;font-weight:700}
.news-card{top:2350px;width:293px;height:382px;background:var(--white);box-shadow:0 2px 12px rgba(0,0,0,.09)}
.news-photo{height:172px}
.news-body{padding:20px 32px 0}
.news-date{color:var(--pink);font-size:14px;font-weight:500;letter-spacing:.5px}
.news-body h4{font-size:15px;font-weight:600;line-height:22px;margin-top:9px;letter-spacing:.5px}
.news-body p{font-size:14px;line-height:19px;color:var(--grey);margin-top:11px}
.news-more{color:var(--pink);font-size:13px;font-weight:600;margin-top:9px}

/* cta */
.cta{left:0;top:2829px;width:1200px;height:403px;background:linear-gradient(110deg,#e8336f,#f3508a 60%,#f0407f)}
.cta-title{left:606px;top:2936px;font-size:28px;font-weight:700;color:var(--white)}
.cta-sub{left:606px;top:2978px;font-size:18px;line-height:30px;color:var(--white)}
.cta-btn{left:604px;top:3067px;width:245px;height:52px;border-radius:26px;background:var(--white);font-size:17px;display:flex;align-items:center;justify-content:center}

/* footer */
.site-footer{left:0;top:3232px;width:1200px;height:439px;background:var(--dark);color:var(--white)}
.footer-h{font-size:14px;font-weight:600}
.field{background:var(--white);color:#666;font-size:13px;padding:0 14px;display:flex;align-items:center}
.field.msg{align-items:flex-start;padding-top:10px}
.links{list-style:none;font-size:13px}
.links li{height:27px;display:flex;align-items:center;gap:6px}
.links li::before{content:"»";color:var(--pink);font-size:15px}
.contact-item{display:flex;gap:10px;font-size:13px;line-height:19px}
.social{width:28px;height:28px;border-radius:50%;border:2px solid var(--white);background:var(--pink)}
.copyright{left:0;top:3605px;width:1200px;height:66px;border-top:2px solid #555;background:var(--darker);text-align:center;line-height:62px;font-size:16px;color:#ddd}
</style>
</head>
<body>

<header class="site-header abs">
  <div class="brand abs">
    <span class="brand-mark"></span>
    <div><div class="brand-name">Visitwell</div><div class="brand-tag">HOME CARE MANAGEMENT</div></div>
  </div>
  <nav class="main-nav abs"><span>PRODUCT</span><span>PRICING</span><span>BLOG</span><span>FAQ</span><span>CONTACT</span></nav>
  <div class="login abs">LOG IN</div>
  <div class="demo-btn abs">BOOK A<strong>FREE DEMO</strong></div>
</header>

<section class="hero">
  <div class="hero-photo abs" role="img" aria-label="Older couple smiling together on a blue sofa, looking at a tablet"></div>
  <svg class="abs" style="left:0;top:83px" width="1200" height="829" viewBox="0 83 1200 829">
    <path d="M0,900 C250,740 620,680 1200,738 L1200,760 C650,712 260,760 0,912 Z" fill="var(--pink-soft)"/>
    <path d="M0,912 C260,760 650,712 1200,760 L1200,912 Z" fill="#fff"/>
  </svg>
  <h1 class="hero-title abs">Quality care<br>from experts<br>you trust</h1>
  <ul class="hero-list abs">
    <li><svg width="24" height="24" viewBox="0 0 24 24"><circle cx="12" cy="12" r="10" fill="none" stroke="var(--pink)" stroke-width="2"/><path d="M7 12l4 4 8-9" fill="none" stroke="var(--pink)" stroke-width="2.4"/></svg>All-in-one home care software</li>
    <li><svg width="24" height="24" viewBox="0 0 24 24"><circle cx="12" cy="12" r="10" fill="none" stroke="var(--pink)" stroke-width="2"/><path d="M7 12l4 4 8-9" fill="none" stroke="var(--pink)" stroke-width="2.4"/></svg>Create staff rotas with automated scheduling tools</li>
    <li><svg width="24" height="24" viewBox="0 0 24 24"><circle cx="12" cy="12" r="10" fill="none" stroke="var(--pink)" stroke-width="2"/><path d="M7 12l4 4 8-9" fill="none" stroke="var(--pink)" stroke-width="2.4"/></svg>Easy to set up and use. Get started today!</li>
  </ul>
  <div class="hero-btn abs">HOW IT WORKS <svg width="18" height="18" viewBox="0 0 18 18"><circle cx="9" cy="9" r="8" fill="#fff"/><path d="M9 5v8M5 9h8" stroke="var(--pink)" stroke-width="2"/></svg></div>
</section>

<section class="welcome abs">
  <h1>Welcome to</h1>
  <h2>Visitwell Home Care Management</h2>
  <p>Lorem Ipsum is simply dummy text of the printing and typesetting industry. Lorem Ipsum has been the industry's standard dummy text ever since the 1500s</p>
</section>

<div class="audiences abs">
  <div class="audience"><div class="icon"><span></span></div><h3>For Managers</h3><p>Lorem Ipsum is simply dummy text of the printing and typesetting industry. Lorem Ipsum has been the industry's standard</p></div>
  <div class="audience"><div class="icon"><span></span></div><h3>For Carers</h3><p>Lorem Ipsum is simply dummy text of the printing and typesetting industry. Lorem Ipsum has been the industry's standard</p></div>
  <div class="audience"><div class="icon"><span></span></div><h3>For Families</h3><p>Lorem Ipsum is simply dummy text of the printing and typesetting industry. Lorem Ipsum has been the industry's standard</p></div>
</div>

<section class="services">
  <svg class="services-band abs" viewBox="0 1340 1200 870" width="1200" height="870">
    <path d="M0,1660 C300,1560 800,1470 1200,1500 L1200,2210 L0,2210 Z" fill="var(--pink)"/>
    <path d="M0,1690 C300,1590 800,1500 1200,1525 L1200,2210 L0,2210 Z" fill="var(--dark)"/>
    <path d="M0,2209 L0,1900 C80,1800 200,1770 330,1775 C480,1782 578,1900 566,2040 C560,2120 532,2180 505,2209 Z" fill="#8a7f79" stroke="var(--darker)" stroke-width="8"/>
  </svg>
  <div class="abs" role="img" aria-label="Smiling older couple holding up a smartphone" style="left:0;top:1775px;width:566px;height:434px;clip-path:path('M0,434 L0,125 C80,25 200,-5 330,0 C480,7 578,125 566,265 C560,345 532,405 505,434 Z');background:linear-gradient(100deg,#d7c3b0,#bfb2a8 45%,#7f7670)"></div>
  <svg class="abs" style="left:288px;top:1957px" width="76" height="76" viewBox="0 0 76 76"><circle cx="38" cy="38" r="38" fill="#262224"/><path d="M30 24l22 14-22 14z" fill="#fff"/></svg>

  <div class="service abs" style="left:141px;top:1375px;width:314px;height:314px">
    <div class="service-photo" role="img" aria-label="Family of three generations looking at a tablet" style="width:274px;height:274px;background:linear-gradient(160deg,#d9c2ae,#8f7a6d)">Digital<br>care plans<span class="go"><svg width="12" height="12" viewBox="0 0 12 12"><path d="M4 2l4 4-4 4" fill="none" stroke="var(--pink)" stroke-width="2"/></svg></span></div>
  </div>
  <div class="service featured abs" style="left:422px;top:1354px;width:356px;height:356px">
    <div class="service-photo" role="img" aria-label="Hands holding a mobile phone" style="width:310px;height:310px;background:linear-gradient(160deg,#8c6a6a,#4a3e40)">Call<br>monitoring<span class="go"><svg width="12" height="12" viewBox="0 0 12 12"><path d="M4 2l4 4-4 4" fill="none" stroke="var(--pink)" stroke-width="2"/></svg></span></div>
  </div>
  <div class="service abs" style="left:749px;top:1375px;width:314px;height:314px">
    <div class="service-photo" role="img" aria-label="Older woman with glasses using a laptop" style="width:274px;height:274px;background:linear-gradient(160deg,#e9e6e2,#7a8fa6)">Risk<br>assessments<span class="go"><svg width="12" height="12" viewBox="0 0 12 12"><path d="M4 2l4 4-4 4" fill="none" stroke="var(--pink)" stroke-width="2"/></svg></span></div>
  </div>

  <h2 class="what-title abs">WHT WE DO?</h2>
  <p class="what-text abs">Lorem Ipsum is simply dummy text of the printing and typesetting industry. Lorem Ipsum has been the industry's standard dummy text ever since the 1500s, when an unknown printer took a galley of type and scrambled it to make.</p>
  <div class="pill abs" style="left:651px;top:2032px;width:170px;height:44px;font-size:17px">Learn More</div>
</section>

<section class="news">
  <h2 class="news-title abs">LATEST NEWS</h2>
  <article class="news-card abs" style="left:131px">
    <div class="news-photo" role="img" aria-label="Older couple embracing and smiling" style="background:linear-gradient(150deg,#ece6df,#b9a89a)"></div>
    <div class="news-body"><div class="news-date">JAN 20, 2020</div><h4>INDUSTRY'S STANDARD<br>DUMMY TEXT EVER</h4><p>Lorem Ipsum is simply dummy text of the printing &amp; typesetting industry. Lorem Ipsum</p><div class="news-more">LEARN MORE ›</div></div>
  </article>
  <article class="news-card abs" style="left:453px">
    <div class="news-photo" role="img" aria-label="Young woman showing a phone to an older couple" style="background:linear-gradient(150deg,#efeae6,#a6978e)"></div>
    <div class="news-body"><div class="news-date">JAN 20, 2020</div><h4>INDUSTRY'S STANDARD<br>DUMMY TEXT EVER</h4><p>Lorem Ipsum is simply dummy text of the printing &amp; typesetting industry. Lorem Ipsum</p><div class="news-more">LEARN MORE ›</div></div>
  </article>
  <article class="news-card abs" style="left:775px">
    <div class="news-photo" role="img" aria-label="Grandmother and granddaughter taking a selfie" style="background:linear-gradient(150deg,#dfe0dc,#8c98a8)"></div>
    <div class="news-body"><div class="news-date">JAN 20, 2020</div><h4>INDUSTRY'S STANDARD<br>DUMMY TEXT EVER</h4><p>Lorem Ipsum is simply dummy text of the printing &amp; typesetting industry. Lorem Ipsum</p><div class="news-more">LEARN MORE ›</div></div>
  </article>
</section>

<section class="cta abs">
  <div class="abs" role="img" aria-label="Smiling older couple listening to music on headphones" style="left:0;top:0;width:452px;height:403px;clip-path:path('M0,0 L370,0 C440,71 470,221 440,301 C420,361 390,403 370,403 L0,403 Z');background:linear-gradient(110deg,#5d5957,#b5a79c 55%,#d9cfc6)"></div>
  <svg class="abs" style="left:0;top:0" width="460" height="403"><path d="M370,0 C440,71 470,221 440,301 C420,361 390,403 370,403" fill="none" stroke="#fff" stroke-width="5"/></svg>
</section>
<h2 class="cta-title abs">Want to know more?</h2>
<p class="cta-sub abs">Request a free assessment and<br>get started today</p>
<div class="cta-btn abs">Book A Free Demo</div>

<footer class="site-footer abs">
  <div class="footer-h abs" style="left:135px;top:65px">GET IN TOUCH</div>
  <div class="field abs" style="left:132px;top:110px;width:219px;height:35px">Your kid's name</div>
  <div class="field abs" style="left:361px;top:110px;width:219px;height:35px">Your kid's age</div>
  <div class="field abs" style="left:132px;top:157px;width:219px;height:34px">Your Email</div>
  <div class="field abs" style="left:361px;top:157px;width:219px;height:34px">Phone Number</div>
  <div class="field msg abs" style="left:132px;top:202px;width:448px;height:72px">Your Message</div>
  <div class="pill abs" style="left:132px;top:288px;width:132px;height:38px;font-size:16px">Send Us</div>

  <div class="footer-h abs" style="left:650px;top:65px">QUICK LINKS</div>
  <ul class="links abs" style="left:650px;top:96px"><li>Product</li><li>Pricing</li><li>Blog</li><li>FAQ</li><li>Contact Us</li></ul>

  <div class="footer-h abs" style="left:834px;top:65px">QUICK LINKS</div>
  <div class="contact-item abs" style="left:834px;top:101px"><svg width="14" height="18" viewBox="0 0 14 18"><path d="M7 1a6 6 0 0 1 6 6c0 4-6 10-6 10S1 11 1 7a6 6 0 0 1 6-6z" fill="none" stroke="var(--pink)" stroke-width="1.6"/><circle cx="7" cy="7" r="2" fill="var(--pink)"/></svg><span>Visitwell<br>Home Care Management</span></div>
  <div class="contact-item abs" style="left:834px;top:155px"><svg width="16" height="16" viewBox="0 0 16 16"><path d="M3 1l3 3-2 2c1 2 3 4 5 5l2-2 3 3-2 3C7 15 1 9 1 3z" fill="var(--pink)"/></svg><span>(305) 555-0142</span></div>
  <div class="contact-item abs" style="left:834px;top:195px"><svg width="16" height="16" viewBox="0 0 16 16"><rect x="1" y="3" width="14" height="10" fill="none" stroke="var(--pink)" stroke-width="1.4"/><path d="M1 3l7 6 7-6" fill="none" stroke="var(--pink)" stroke-width="1.4"/></svg><span>contact@visitwell-care.com</span></div>

  <div class="footer-h abs" style="left:650px;top:270px">STAY CONNECTED</div>
  <span class="social abs" style="left:800px;top:264px"></span>
  <span class="social abs" style="left:834px;top:264px"></span>
  <span class="social abs" style="left:868px;top:264px"></span>
  <span class="social abs" style="left:904px;top:264px"></span>
</footer>
<div class="copyright abs">© 2020 Visitwell | All Rights are Reserved | Terms and Conditions</div>

</body>
</html>
```